Stylish Design With Simple UI For Appointment Site

Note: Logo file now attached. Extra credit to anyone who offers basic HTML templates in the final deliverable, incorporating the individual components of the design (using DIVs and CSS).

There are two key requirements for this site:

1. It makes our site look like one of the most professional of its kind. We want to look the part;
2. It has a very simple, straight-forward user interface. We're nothing without being intuitive.

Our site will be used by other businesses to set up their own online booking systems.

Logo samples attached. The colour scheme is not yet set but two possible options are:

1. Dark (#323B3A) & Blue (#12B5D4) on White background
2. White & Yellow (#FEF102) on Grey (#3A3A3C) background

For inspiration, and an idea of what we like, take a look at quillbarn.com - it's very clear and eye-catching, although its pages are longer than we would like ours to be. Oh but we don't need a chimp! Instead of the section with the chimp in, we would like a changing image headline section on the home page, in the style of fellgarde.co.uk (with a less high image; we have attached one image which you may want to try out with this, but happy to see other ideas).

Any graphics included must be royalty free and free for commercial use. Fonts should be readily available and specified.

We would like to see the design applied to the following pages:

1. The main public home page (features header, login prompt, menu, changing image banner with headlines, main body, footer menu).
2. A secondary public page (features a similar layout to home page but without image headline banner, includes extra panels/body detail).
3. The Control Panel page (features several list panels and an add appointment button).
4. A list-style administration page (with popup item editor window).
5. A settings administration page (with form).

In that order, a sample walk-through design spec will be attached.

To summarise, we are looking for someone to put forward not only a design but something which also focuses on the user interface. The designer should consider all of the examples and guidance given, but shouldn't let that limit any innovation.

Happy to respond to any questions and give constant feedback.

Thank you.

-*-*-*-*-*-*-*-*-*-*-*-*-*-*-*-*-

Update, 18th Nov 2011:

1. I'm about the upload the logos so you can incorporate these into your designs.

2. A UI question of mine is how to move from a list view (e.g. Resources) to editing one of those items in the list. In the spec document I showed a popup editor for these items but I don't know if that's the best thing to do. Happy to see other ideas on this - whatever the best user experience would be.

3. On the designs in the spec document I've not included any help functionality. It would be good to include pieces of guidance on each page of the administration area to help the user - guess these could either be info panels on the pages themselves or info popups. Again, would be good to see some ideas in the designs.

Also, just to be clear, I am really looking for something that looks like a modern innovative "web app" rather than it looking like a promotional corporate web site.

Target Market(s)

Owners of businesses of all types (e.g. salons, small hotels, surgeries, etc).

Industry/Entity Type

Commercial

Requirements
Must have
• Headline image transition panel on home page.

Layout, graphic and font styles along similar lines to quillbarn.com, fellgarde.co.uk, etc.
Nice to have
• Blog feed panel on the home page.

Innovative ideas for improvements to the spec.
Should not have
• Anything which can't be practically rendered when the design is converted to HTML.

Should not be overly influenced by the layout and style in the attached spec - that should just be a guide to the content and layout of the site.

```html
<!DOCTYPE html>
<html lang="en">
<head>
<meta charset="utf-8">
<title>Slotwise – Home</title>
<link rel="stylesheet" href="https://fonts.googleapis.com/css2?family=Open+Sans:wght@400;600;700&family=Arimo:wght@400;700&display=swap">
<style>
:root{
  --blue:#12B5D4;
  --blue-dark:#0E7E94;
  --dark:#323B3A;
  --footer:#252E2F;
  --text:#2b2b2b;
  --muted:#666;
  --line:#d6d6d6;
  --bubble:#efefef;
}
*{box-sizing:border-box;margin:0;padding:0}
html,body{width:1167px;height:1200px;overflow:hidden}
body{position:relative;background:#fff;font-family:"Arimo",Arial,sans-serif;color:var(--text);font-size:13px}
.abs{position:absolute}
.page-top{left:0;top:0;width:1167px;height:110px;background:linear-gradient(#f4fafc,#fff)}

/* brand */
.brand{left:60px;top:62px;display:flex;align-items:center;gap:12px}
.brand-mark{width:34px;height:34px;background:var(--blue)}
.brand-name{font-family:"Open Sans",sans-serif;font-weight:600;font-size:32px;color:var(--dark);letter-spacing:.5px}

/* header tools */
.login-label{left:494px;top:37px;font-family:"Open Sans",sans-serif;font-size:11.5px;color:#444}
.field{height:28px;border:1px solid #cfe3ea;border-radius:4px;background:#fff;padding:0 9px;font-size:11.5px;color:#b4b4b4;display:flex;align-items:center;font-family:"Open Sans",sans-serif}
.field-user{left:494px;top:59px;width:141px}
.field-pass{left:643px;top:59px;width:141px}
.btn-login{left:795px;top:59px;width:64px;height:28px;border-radius:4px;background:linear-gradient(#27c4e0,#0ea8c6);color:#fff;font-family:"Open Sans",sans-serif;font-size:13px;display:flex;align-items:center;justify-content:center}
.header-sep{left:875px;top:60px;width:1px;height:26px;background:#ddd}
.field-search{left:893px;top:59px;width:207px;justify-content:space-between}
.util-links{right:67px;top:36px;display:flex;gap:7px;font-family:"Open Sans",sans-serif;font-size:11.5px;color:#444;align-items:center}
.util-links .dot{width:3px;height:3px;border-radius:50%;background:var(--blue)}

/* main nav */
.main-nav{left:306px;top:102px;width:794px;height:45px;border-radius:4px;background:linear-gradient(#1ec3df,#0aa3c2);overflow:hidden}
.main-nav a{position:absolute;top:0;height:45px;line-height:45px;color:#fff;text-decoration:none;font-family:"Open Sans",sans-serif;font-size:12.5px;transform:translateX(-50%)}
.main-nav .active{left:0;width:94px;transform:none;text-align:center;background:var(--blue-dark)}

/* hero */
.hero{left:60px;top:161px;width:1040px;height:367px;border-radius:4px;overflow:hidden;
  background:linear-gradient(90deg,#1e2d48 0%,#2a3a58 26%,#b9b4a8 30%,#d9d2c2 42%,#c4cbc8 55%,#a9b6bb 68%,#8a9ea5 100%)}
.hero-caption{left:744px;top:161px;width:325px;height:367px;background:rgba(120,120,120,.55)}
.hero-strip{left:1069px;top:161px;width:31px;height:367px;background:#9a6f5a;border-radius:0 4px 4px 0;opacity:.6}
.hero-title{left:774px;top:190px;width:290px;font-family:"Open Sans",sans-serif;font-weight:700;font-size:28px;line-height:35px;color:#fff;letter-spacing:-.8px;text-shadow:0 1px 2px rgba(0,0,0,.35)}
.hero-text{left:775px;top:277px;width:250px;font-size:13.2px;line-height:16px;color:#fff}
.hero-more{left:775px;top:352px;font-size:12px;color:var(--blue);font-weight:700;text-decoration:underline;display:flex;align-items:center;gap:5px}
.hero-more::before{content:"";border-left:5px solid #fff;border-top:4px solid transparent;border-bottom:4px solid transparent}
.hero-dots{left:839px;top:475px;display:flex;gap:21px}
.hero-dots span{width:12px;height:12px;border-radius:50%;background:#2a2a2a;box-shadow:inset 0 1px 2px #000,0 1px 0 rgba(255,255,255,.3)}
.hero-dots .on{background:#fff}

/* content */
.side-bg{left:744px;top:602px;width:356px;height:400px;background:linear-gradient(90deg,#f3f3f3,#fff 12%)}
.section-title{font-family:"Open Sans",sans-serif;font-size:23px;color:var(--dark)}
.sub-title{font-family:"Open Sans",sans-serif;font-size:18.5px;color:var(--dark)}
.sub-title em,.stat{font-style:normal;color:var(--blue)}
.rule{height:1px;background:var(--line)}
.copy{font-size:13px;line-height:16px;color:#222}
.benefits{list-style:none;font-size:13px;color:#222}
.benefits li{height:21.7px;display:flex;align-items:center;gap:8px}
.benefits li::before{content:"";border-left:6px solid var(--blue);border-top:4px solid transparent;border-bottom:4px solid transparent}

.news-title{font-family:"Open Sans",sans-serif;font-size:14px;color:var(--blue)}
.news-text{font-size:13px;line-height:15px;color:#222;width:290px}
.news-sep{left:771px;top:689px;width:329px;border-top:1px dotted #ccc}
.view-more{font-size:12px;color:var(--blue);text-decoration:underline}

.quote{left:815px;width:285px;height:66px;background:var(--bubble);border-radius:5px;padding:11px 11px;font-size:12px;line-height:14px;color:#222}
.quote::before{content:"";position:absolute;left:-6px;top:10px;border-right:6px solid var(--bubble);border-top:6px solid transparent;border-bottom:6px solid transparent}
.quote .who{display:block;margin-top:6px;color:var(--blue);font-size:11.5px}
.avatar{left:773px;width:33px;height:33px;border:2px solid #ddd;background:linear-gradient(#8fb36a,#c9a27c)}

/* footer */
.site-footer{left:0;top:1070px;width:1167px;height:130px;background:var(--footer)}
.foot-nav{left:61px;top:1113px;display:flex;gap:10px;align-items:center;font-family:"Open Sans",sans-serif;font-size:13px;color:#aab0b0}
.foot-nav .current{color:#fff}
.foot-nav .dot{width:3px;height:3px;border-radius:50%;background:#8a9090}
.copyright{left:61px;top:1139px;font-family:"Open Sans",sans-serif;font-size:11.5px;color:#aab0b0}
.follow{left:868px;top:1118px;font-family:"Open Sans",sans-serif;font-weight:700;font-size:13px;color:#fff}
.social{top:1113px;width:27px;height:27px;border-radius:4px}
</style>
</head>
<body>
<div class="abs page-top"></div>

<header>
  <div class="abs brand"><span class="brand-mark"></span><span class="brand-name">Slotwise</span></div>

  <div class="abs login-label">Login to Slotwise</div>
  <div class="abs field field-user">Username</div>
  <div class="abs field field-pass">Password</div>
  <div class="abs btn-login">Login</div>
  <div class="abs header-sep"></div>
  <div class="abs field field-search">Search
    <svg width="15" height="15" viewBox="0 0 15 15"><circle cx="6" cy="6" r="4.5" fill="none" stroke="#12B5D4" stroke-width="2.2"/><line x1="9.3" y1="9.3" x2="13.5" y2="13.5" stroke="#12B5D4" stroke-width="2.6" stroke-linecap="round"/></svg>
  </div>
  <nav class="abs util-links"><span>Login</span><i class="dot"></i><span>Help</span><i class="dot"></i><span>FAQs</span><i class="dot"></i><span>Sitemap</span></nav>

  <nav class="abs main-nav">
    <a class="active" href="#">HOME</a>
    <a href="#" style="left:141px">WORK</a>
    <a href="#" style="left:220px">BLOG</a>
    <a href="#" style="left:315px">PRODUCTS</a>
    <a href="#" style="left:422px">SERVICES</a>
    <a href="#" style="left:525px">SUPPORT</a>
    <a href="#" style="left:616px">ABOUT</a>
    <a href="#" style="left:717px">CONTACT US</a>
  </nav>
</header>

<section>
  <div class="abs hero" role="img" aria-label="Photo of a person carrying shopping bags in a blurred street"></div>
  <div class="abs hero-caption"></div>
  <div class="abs hero-strip"></div>
  <h1 class="abs hero-title">Lorem ipsum dolor sit amet</h1>
  <p class="abs hero-text">Ut wisi enim ad minim veniam, quis nostrud exerci tation ullamcorper suscipit lobortis nisl ut aliquip ex ea commodo consequat.</p>
  <a class="abs hero-more">Read more</a>
  <div class="abs hero-dots"><span class="on"></span><span></span><span></span><span></span></div>
</section>

<div class="abs side-bg"></div>

<main>
  <h2 class="abs section-title" style="left:60px;top:553px">Slotwise</h2>
  <div class="abs rule" style="left:60px;top:601px;width:1040px"></div>

  <h3 class="abs sub-title" style="left:60px;top:631px"><span class="stat">173,348</span> booking in 161 countries worldwide</h3>
  <p class="abs copy" style="left:59px;top:667px;width:640px">Lorem ipsum dolor sit amet, consectetuer adipiscing elit, sed diam nonummy nibh euismod tincidunt ut laoreet dolore magna aliquam erat volutpat. Ut wisi enim ad minim veniam, quis nostrud exerci tation ullamcorper suscipit lobortis nisl ut aliquip ex ea commodo consequat.</p>

  <h3 class="abs sub-title" style="left:60px;top:751px">Your <em>benefit</em></h3>
  <p class="abs copy" style="left:59px;top:786px;width:650px">Duis autem vel eum iriure dolor in hendrerit in vulputate velit esse molestie consequat, vel illum dolore eu feugiat nulla facilisis at vero eros et accumsan et iusto odio dignissim qui blandit praesent luptatum zzril delenit augue duis dolore te feugait nulla facilisi.</p>

  <ul class="abs benefits" style="left:59px;top:856px">
    <li>Lorem ipsum dolor sit amet, consectetuer adipiscing elit.</li>
    <li>Accumsan et iusto odio dignissim qui blandit</li>
    <li>Ut wisi enim ad minim veniam</li>
    <li>Vulputate velit esse molestie consequat</li>
  </ul>
</main>

<aside>
  <h2 class="abs sub-title" style="left:771px;top:558px">What News ?</h2>

  <div class="abs" style="left:773px;top:628px">
    <div class="news-title">Save 50% or more with Flash Deals</div>
    <p class="news-text">Lorem ipsum dolor sit amet, consectetuer adipiscing elit, sed diam nonummy nibh.</p>
  </div>
  <div class="abs news-sep"></div>
  <div class="abs" style="left:773px;top:699px">
    <div class="news-title">Booking on your smartphone</div>
    <p class="news-text">ulputate velit esse molestie consequat, vel illum dolore eu</p>
  </div>
  <a class="abs view-more" style="left:773px;top:767px">View more</a>

  <h2 class="abs sub-title" style="left:771px;top:809px">Testimonials</h2>
  <div class="abs rule" style="left:744px;top:851px;width:356px"></div>

  <div class="abs avatar" style="top:879px" role="img" aria-label="Customer portrait"></div>
  <blockquote class="abs quote" style="top:878px">Lorem ipsum dolor sit amet, consectetuer adipiscing elit, sed diam.<span class="who">Tobias</span></blockquote>

  <div class="abs avatar" style="top:955px" role="img" aria-label="Customer portrait"></div>
  <blockquote class="abs quote" style="top:954px">Lorem ipsum dolor sit amet, consectetuer adipiscing elit, sed diam.<span class="who">Tobias</span></blockquote>
</aside>

<footer>
  <div class="abs site-footer"></div>
  <nav class="abs foot-nav">
    <span class="current">Home</span><i class="dot"></i><span>Work</span><i class="dot"></i><span>Blog</span><i class="dot"></i><span>Products</span><i class="dot"></i><span>Services</span><i class="dot"></i><span>Support</span><i class="dot"></i><span>About</span><i class="dot"></i><span>Contact us</span>
  </nav>
  <div class="abs copyright">Copyright © 2011 Slotwise. All right reserved.</div>
  <div class="abs follow">Follow Us</div>
  <span class="abs social" style="left:958px;background:#4a64a0" aria-label="Social network"></span>
  <span class="abs social" style="left:991px;background:#3fb8e6" aria-label="Social network"></span>
  <span class="abs social" style="left:1023px;background:#2a7fb8" aria-label="Social network"></span>
  <span class="abs social" style="left:1056px;background:#f08a24" aria-label="News feed"></span>
</footer>
</body>
</html>
```